Fun A1 2012 family planner using clever typography and block colour

I have been looking for an A1 2012 family planner and I have not been able to find one. Hence I would like help to develop such a planner. I plan to print it on matt paper, portrait orientated. I have attached some reference pictures of our 2011 planner. I like interesting typography, clear clean colours and simple illustration. I need space to write in daily events and need the weeks and days to be clearly delineated from each other. Each day cell needs the date and day in it (please refer to the file uploaded for a visual reference confirming this). Each weekend needs some kind of colour/ typographic delineation. I want a design for a year-at-a-view calendar. I plan to print the planner in Sydney, Australia with plinthworkprints.com.au and probably to sell printed copies online. The terms & conditions of this project are that I will own the design concept 100% and in perpetuity worldwide once payment has been made. (NB. The attached Work File in Word contains a rough layout and all months, days and dates all typed up to make for quicker design.)

Target Market(s)

Reasonably well heeled family of 4. 2 parents. 2 kids. 2 pets.

Industry/Entity Type

Events

Requirements
Must have
• The calendar must be portrait (not landscape orientated), A1 size. It will be printed on matt paper by plinthworkprints.com.au. It must have months running left to right (Jan-Dec) and day/date cells running top to bottom (refer 2011 planner photos in file uploaded). The day/ date cells must be around 3(w)x2(h)cm - big enough to write daily events in. Weekends must be colour/ typographically delineated. 2012 year must be noted as must "A Lanternmoss Inc Project" and web address in fine print bottom left hand left hand corner.
Nice to have
• A Lanternmoss Inc logo in bottom left hand corder (perhaps Nimble Heron like: http://www.artquarry.com/design_submission.aspx?designid=614307). Header/Footer space for customisation (e.g. "Dunmore-Pratt 2012 Planner" or "XYZ Co 2012 Planner".
Should not have
• The calendar should not use photographs or resemble standard or cheesy wall calendars. No watermarks please.

```html
<!DOCTYPE html>
<html lang="en">
<head>
<meta charset="utf-8">
<title>2012 Family Planner</title>
<link rel="stylesheet" href="https://fonts.googleapis.com/css2?family=Lobster&family=Open+Sans:wght@600;700&display=swap">
<style>
:root{
  --sky:#a6dbe6;
  --sky-light:#d4f0f5;
  --hill:#c6dc6b;
  --hill-dark:#b2cd55;
  --band-top:#fcc419;
  --band-bottom:#f0a500;
  --band-line:#d98e00;
  --month-ink:#ffffff;
  --month-shadow:#8a5a00;
  --panel-top:#f4f4f4;
  --panel-bottom:#c9c9c9;
  --rule:#555555;
  --ink:#4a4a4a;
  --weekend:#d07f00;
  --accent:#6cbf2a;
  --scene-a:#f2dcb8;
  --scene-b:#f7c88a;
  --fine:#4f5e1e;
}
*{box-sizing:border-box;margin:0;padding:0}
html,body{width:848px;height:1200px;overflow:hidden}
body{
  position:relative;
  font-family:"Open Sans",Arial,sans-serif;
  background:linear-gradient(100deg,var(--sky) 0%,var(--sky-light) 55%,var(--sky) 100%);
}
.hill{position:absolute;left:0;bottom:0;width:848px;height:120px}
.scenery{
  position:absolute;left:690px;top:1040px;width:158px;height:90px;
  background:linear-gradient(180deg,var(--scene-a),var(--scene-b));
  opacity:.85;
}
.month-band{
  position:absolute;left:24px;top:0;width:656px;height:30px;
  background:linear-gradient(var(--band-top),var(--band-bottom));
  box-shadow:0 2px 3px rgba(0,0,0,.25);
}
.month-band span{
  position:absolute;top:0;height:30px;line-height:28px;transform:translateX(-50%);
  font-family:"Lobster",cursive;font-size:19px;color:var(--month-ink);
  text-shadow:1px 1px 0 var(--month-shadow);
}
.month-band i{position:absolute;top:0;width:1px;height:30px;background:var(--band-line)}
.planner{
  position:absolute;left:24px;top:36px;width:656px;height:1132px;
  background:linear-gradient(var(--panel-top),var(--panel-bottom));
  box-shadow:0 6px 14px rgba(0,0,0,.35);
}
.first-row-rule{position:absolute;left:0;right:0;top:40px;height:1px;background:var(--rule)}
.jan-rule{position:absolute;left:53px;top:0;bottom:0;width:1px;background:var(--rule)}
.month{position:absolute;top:4px;list-style:none;left:var(--x)}
.month li{height:36.2px;font-size:10px;font-weight:600;color:var(--ink);line-height:18px}
.month li i{display:block;font-style:normal;font-weight:700;font-size:10.5px}
.month li.w i{color:var(--weekend)}
.month li.today{color:var(--accent)}
.fine-print{
  position:absolute;left:26px;top:1178px;
  font-size:9px;font-weight:600;color:var(--fine);letter-spacing:.2px;
}
.fine-print b{font-weight:700}
</style>
</head>
<body>
<svg class="hill" viewBox="0 0 848 120" preserveAspectRatio="none" aria-hidden="true">
  <path d="M0 60 Q300 20 600 40 T848 20 V120 H0Z" fill="var(--hill)"/>
  <path d="M0 95 Q400 70 848 90 V120 H0Z" fill="var(--hill-dark)"/>
</svg>
<div class="scenery" role="img" aria-label="Illustration of cartoon rocks on the hill"></div>

<div class="month-band">
  <span style="left:23px">Jan</span><i style="left:53px"></i>
  <span style="left:85px">Feb</span><i style="left:114px"></i>
  <span style="left:145px">Mar</span><i style="left:170px"></i>
  <span style="left:198px">Apr</span><i style="left:223px"></i>
  <span style="left:250px">May</span><i style="left:276px"></i>
  <span style="left:301px">Jun</span><i style="left:326px"></i>
  <span style="left:347px">Jul</span><i style="left:373px"></i>
  <span style="left:397px">Aug</span><i style="left:424px"></i>
  <span style="left:451px">Sep</span><i style="left:478px"></i>
  <span style="left:502px">Oct</span><i style="left:527px"></i>
  <span style="left:557px">Nov</span><i style="left:583px"></i>
  <span style="left:611px">Dec</span>
</div>

<main class="planner">
  <div class="first-row-rule"></div>
  <div class="jan-rule"></div>

  <ul class="month" style="--x:15px">
    <li class="w">1<i>SUN</i></li><li>2<i>MON</i></li><li>3<i>TUE</i></li><li>4<i>WED</i></li><li>5<i>THU</i></li><li>6<i>FRI</i></li><li class="w">7<i>SAT</i></li>
    <li class="w today">8<i>SUN</i></li><li>9<i>MON</i></li><li>10<i>TUE</i></li><li>11<i>WED</i></li><li>12<i>THU</i></li><li>13<i>FRI</i></li><li class="w">14<i>SAT</i></li>
    <li class="w">15<i>SUN</i></li><li>16<i>MON</i></li><li>17<i>TUE</i></li><li>18<i>WED</i></li><li>19<i>THU</i></li><li>20<i>FRI</i></li><li class="w">21<i>SAT</i></li>
    <li class="w">22<i>SUN</i></li><li>23<i>MON</i></li><li>24<i>TUE</i></li><li>25<i>WED</i></li><li>26<i>THU</i></li><li>27<i>FRI</i></li><li class="w">28<i>SAT</i></li>
    <li class="w">29<i>SUN</i></li><li>30<i>MON</i></li><li>31<i>TUE</i></li>
  </ul>

  <ul class="month" style="--x:76px">
    <li>1<i>WED</i></li><li>2<i>THU</i></li><li>3<i>FRI</i></li><li class="w">4<i>SAT</i></li><li class="w">5<i>SUN</i></li><li>6<i>MON</i></li><li>7<i>TUE</i></li>
    <li>8<i>WED</i></li><li>9<i>THU</i></li><li>10<i>FRI</i></li><li class="w">11<i>SAT</i></li><li class="w">12<i>SUN</i></li><li>13<i>MON</i></li><li>14<i>TUE</i></li>
    <li>15<i>WED</i></li><li>16<i>THU</i></li><li>17<i>FRI</i></li><li class="w">18<i>SAT</i></li><li class="w">19<i>SUN</i></li><li>20<i>MON</i></li><li>21<i>TUE</i></li>
    <li>22<i>WED</i></li><li>23<i>THU</i></li><li>24<i>FRI</i></li><li class="w">25<i>SAT</i></li><li class="w">26<i>SUN</i></li><li>27<i>MON</i></li><li>28<i>TUE</i></li>
    <li>29<i>WED</i></li>
  </ul>

  <ul class="month" style="--x:135px">
    <li>1<i>THU</i></li><li>2<i>FRI</i></li><li class="w">3<i>SAT</i></li><li class="w">4<i>SUN</i></li><li>5<i>MON</i></li><li>6<i>TUE</i></li><li>7<i>WED</i></li>
    <li>8<i>THU</i></li><li>9<i>FRI</i></li><li class="w">10<i>SAT</i></li><li class="w">11<i>SUN</i></li><li>12<i>MON</i></li><li>13<i>TUE</i></li><li>14<i>WED</i></li>
    <li>15<i>THU</i></li><li>16<i>FRI</i></li><li class="w">17<i>SAT</i></li><li class="w">18<i>SUN</i></li><li>19<i>MON</i></li><li>20<i>TUE</i></li><li>21<i>WED</i></li>
    <li>22<i>THU</i></li><li>23<i>FRI</i></li><li class="w">24<i>SAT</i></li><li class="w">25<i>SUN</i></li><li>26<i>MON</i></li><li>27<i>TUE</i></li><li>28<i>WED</i></li>
    <li>29<i>THU</i></li><li>30<i>FRI</i></li><li class="w">31<i>SAT</i></li>
  </ul>

  <ul class="month" style="--x:190px">
    <li class="w">1<i>SUN</i></li><li>2<i>MON</i></li><li>3<i>TUES</i></li><li>4<i>WED</i></li><li>5<i>THU</i></li><li>6<i>FRI</i></li><li class="w">7<i>SAT</i></li>
    <li class="w">8<i>SUN</i></li><li>9<i>MON</i></li><li>10<i>TUES</i></li><li>11<i>WED</i></li><li>12<i>THU</i></li><li>13<i>FRI</i></li><li class="w">14<i>SAT</i></li>
    <li class="w">15<i>SUN</i></li><li>16<i>MON</i></li><li>17<i>TUE</i></li><li>18<i>WED</i></li><li>19<i>THU</i></li><li>20<i>FRI</i></li><li class="w">21<i>SAT</i></li>
    <li class="w">22<i>SUN</i></li><li>23<i>MON</i></li><li>24<i>TUE</i></li><li>25<i>WED</i></li><li>26<i>THU</i></li><li>27<i>FRI</i></li><li class="w">28<i>SAT</i></li>
    <li class="w">29<i>SUN</i></li><li>30<i>MON</i></li>
  </ul>

  <ul class="month" style="--x:242px">
    <li>1<i>TUES</i></li><li>2<i>WED</i></li><li>3<i>THU</i></li><li>4<i>FRI</i></li><li class="w">5<i>SAT</i></li><li class="w">6<i>SUN</i></li><li>7<i>MON</i></li>
    <li>8<i>TUE</i></li><li>9<i>WED</i></li><li>10<i>THU</i></li><li>11<i>FRI</i></li><li class="w">12<i>SAT</i></li><li class="w">13<i>SUN</i></li><li>14<i>MON</i></li>
    <li>15<i>TUE</i></li><li>16<i>WED</i></li><li>17<i>THU</i></li><li>18<i>FRI</i></li><li class="w">19<i>SAT</i></li><li class="w">20<i>SUN</i></li><li>21<i>MON</i></li>
    <li>22<i>TUE</i></li><li>23<i>WED</i></li><li>24<i>THU</i></li><li>25<i>FRI</i></li><li class="w">26<i>SAT</i></li><li class="w">27<i>SUN</i></li><li>28<i>MON</i></li>
    <li>29<i>TUE</i></li><li>30<i>WED</i></li><li>31<i>THU</i></li>
  </ul>

  <ul class="month" style="--x:295px">
    <li>1<i>FRI</i></li><li class="w">2<i>SAT</i></li><li class="w">3<i>SUN</i></li><li>4<i>MON</i></li><li>5<i>TUE</i></li><li>6<i>WED</i></li><li>7<i>THU</i></li>
    <li>8<i>FRI</i></li><li class="w">9<i>SAT</i></li><li class="w">10<i>SUN</i></li><li>11<i>MON</i></li><li>12<i>TUE</i></li><li>13<i>WED</i></li><li>14<i>THU</i></li>
    <li>15<i>FRI</i></li><li class="w">16<i>SAT</i></li><li class="w">17<i>SUN</i></li><li>18<i>MON</i></li><li>19<i>TUE</i></li><li>20<i>WED</i></li><li>21<i>THU</i></li>
    <li>22<i>FRI</i></li><li class="w">23<i>SAT</i></li><li class="w">24<i>SUN</i></li><li>25<i>MON</i></li><li>26<i>TUE</i></li><li>27<i>WED</i></li><li>28<i>THU</i></li>
    <li>29<i>FRI</i></li><li class="w">30<i>SAT</i></li>
  </ul>

  <ul class="month" style="--x:339px">
    <li class="w">1<i>SUN</i></li><li>2<i>MON</i></li><li>3<i>TUE</i></li><li>4<i>WED</i></li><li>5<i>THU</i></li><li>6<i>FRI</i></li><li class="w">7<i>SAT</i></li>
    <li class="w">8<i>SUN</i></li><li>9<i>MON</i></li><li>10<i>TUE</i></li><li>11<i>WED</i></li><li>12<i>THU</i></li><li>13<i>FRI</i></li><li class="w">14<i>SAT</i></li>
    <li class="w">15<i>SUN</i></li><li>16<i>MON</i></li><li>17<i>TUE</i></li><li>18<i>WED</i></li><li>19<i>THU</i></li><li>20<i>FRI</i></li><li class="w">21<i>SAT</i></li>
    <li class="w">22<i>SUN</i></li><li>23<i>MON</i></li><li>24<i>TUE</i></li><li>25<i>WED</i></li><li>26<i>THU</i></li><li>27<i>FRI</i></li><li class="w">28<i>SAT</i></li>
    <li class="w">29<i>SUN</i></li><li>30<i>MON</i></li><li>31<i>TUE</i></li>
  </ul>

  <ul class="month" style="--x:388px">
    <li>1<i>WED</i></li><li>2<i>THU</i></li><li>3<i>FRI</i></li><li class="w">4<i>SAT</i></li><li class="w">5<i>SUN</i></li><li>6<i>MON</i></li><li>7<i>TUE</i></li>
    <li>8<i>WED</i></li><li>9<i>THU</i></li><li>10<i>FRI</i></li><li class="w">11<i>SAT</i></li><li class="w">12<i>SUN</i></li><li>13<i>MON</i></li><li>14<i>TUE</i></li>
    <li>15<i>WED</i></li><li>16<i>THU</i></li><li>17<i>FRI</i></li><li class="w">18<i>SAT</i></li><li class="w">19<i>SUN</i></li><li>20<i>MON</i></li><li>21<i>TUE</i></li>
    <li>22<i>WED</i></li><li>23<i>THU</i></li><li>24<i>FRI</i></li><li class="w">25<i>SAT</i></li><li class="w">26<i>SUN</i></li><li>27<i>MON</i></li><li>28<i>TUE</i></li>
    <li>29<i>WED</i></li><li>30<i>THU</i></li><li>31<i>FRI</i></li>
  </ul>

  <ul class="month" style="--x:439px">
    <li class="w">1<i>SAT</i></li><li class="w">2<i>SUN</i></li><li>3<i>MON</i></li><li>4<i>TUES</i></li><li>5<i>WED</i></li><li>6<i>THU</i></li><li>7<i>FRI</i></li>
    <li class="w">8<i>SAT</i></li><li class="w">9<i>SUN</i></li><li>10<i>MON</i></li><li>11<i>TUE</i></li><li>12<i>WED</i></li><li>13<i>THU</i></li><li>14<i>FRI</i></li>
    <li class="w">15<i>SAT</i></li><li class="w">16<i>SUN</i></li><li>17<i>MON</i></li><li>18<i>TUE</i></li><li>19<i>WED</i></li><li>20<i>THU</i></li><li>21<i>FRI</i></li>
    <li class="w">22<i>SAT</i></li><li class="w">23<i>SUN</i></li><li>24<i>MON</i></li><li>25<i>TUE</i></li><li>26<i>WED</i></li><li>27<i>THU</i></li><li>28<i>FRI</i></li>
    <li class="w">29<i>SAT</i></li><li class="w">30<i>SUN</i></li>
  </ul>

  <ul class="month" style="--x:493px">
    <li>1<i>MON</i></li><li>2<i>TUE</i></li><li>3<i>WED</i></li><li>4<i>THU</i></li><li>5<i>FRI</i></li><li class="w">6<i>SAT</i></li><li class="w">7<i>SUN</i></li>
    <li>8<i>MON</i></li><li>9<i>TUE</i></li><li>10<i>WED</i></li><li>11<i>THU</i></li><li>12<i>FRI</i></li><li class="w">13<i>SAT</i></li><li class="w">14<i>SUN</i></li>
    <li>15<i>MON</i></li><li>16<i>TUE</i></li><li>17<i>WED</i></li><li>18<i>THU</i></li><li>19<i>FRI</i></li><li class="w">20<i>SAT</i></li><li class="w">21<i>SUN</i></li>
    <li>22<i>MON</i></li><li>23<i>TUE</i></li><li>24<i>WED</i></li><li>25<i>THU</i></li><li>26<i>FRI</i></li><li class="w">27<i>SAT</i></li><li class="w">28<i>SUN</i></li>
    <li>29<i>MON</i></li><li>30<i>TUES</i></li><li>31<i>WED</i></li>
  </ul>

  <ul class="month" style="--x:542px">
    <li>1<i>THU</i></li><li>2<i>FRI</i></li><li class="w">3<i>SAT</i></li><li class="w">4<i>SUN</i></li><li>5<i>MON</i></li><li>6<i>TUE</i></li><li>7<i>WED</i></li>
    <li>8<i>THU</i></li><li>9<i>FRI</i></li><li class="w">10<i>SAT</i></li><li class="w">11<i>SUN</i></li><li>12<i>MON</i></li><li>13<i>TUE</i></li><li>14<i>WED</i></li>
    <li>15<i>THU</i></li><li>16<i>FRI</i></li><li class="w">17<i>SAT</i></li><li class="w">18<i>SUN</i></li><li>19<i>MON</i></li><li>20<i>TUE</i></li><li>21<i>WED</i></li>
    <li>22<i>THU</i></li><li>23<i>FRI</i></li><li class="w">24<i>SAT</i></li><li class="w">25<i>SUN</i></li><li>26<i>MON</i></li><li>27<i>TUE</i></li><li>28<i>WED</i></li>
    <li>29<i>THU</i></li><li>30<i>FRI</i></li>
  </ul>

  <ul class="month" style="--x:598px">
    <li class="w">1<i>SAT</i></li><li class="w">2<i>SUN</i></li><li>3<i>MON</i></li><li>4<i>TUES</i></li><li>5<i>WED</i></li><li>6<i>THU</i></li><li>7<i>FRI</i></li>
    <li class="w">8<i>SAT</i></li><li class="w">9<i>SUN</i></li><li>10<i>MON</i></li><li>11<i>TUE</i></li><li>12<i>WED</i></li><li>13<i>THU</i></li><li>14<i>FRI</i></li>
    <li class="w">15<i>SAT</i></li><li class="w">16<i>SUN</i></li><li>17<i>MON</i></li><li>18<i>TUE</i></li><li>19<i>WED</i></li><li>20<i>THU</i></li><li>21<i>FRI</i></li>
    <li class="w">22<i>SAT</i></li><li class="w">23<i>SUN</i></li><li>24<i>MON</i></li><li>25<i>TUE</i></li><li>26<i>WED</i></li><li>27<i>THU</i></li><li>28<i>FRI</i></li>
    <li class="w">29<i>SAT</i></li><li class="w">30<i>SUN</i></li><li>31<i>MON</i></li>
  </ul>
</main>

<p class="fine-print"><b>2012</b> Family Planner · A Lanternmoss Inc Project · plinthworkprints.com.au</p>
</body>
</html>
```